Thank You For Shopping / Hair Care Tips

I need “Thank You For Shopping”
Post cards made for my hair business !
I added pictures of post cards that I really like . I also added my LuzeKora Wigs logo for you guys to use

I want the backside of the flyer to have hair care tips !
I want people to have full directions on how to care for their wigs

Target Market(s)

Im marking to young woman to older middle aged woman
Ages 23-66 . I want my flyer to look mature And classy

Industry/Entity Type

Hair And Beauty

Font styles to use
Serif
Script

Colors
e34699
e34298
e34398

Requirements
Must have
• The flyer must have the Instagram logo with my Instagram name next to it @luze.kora.wigs__
• Also it must have my “Luze Kora Wigs” logo that I’ve uploaded in the pictures section .
• Flyer had to be two sides . One side “ thank you for shopping “ side two “hair care tips”
• My website must be on the flyer - www.luzekorawigs.example
• The flyer must match the colors of my logo
• All white . With the pink and glitter sliver you see on my logo
Nice to have
• Nice to have a glitter border
Should not have
• The flyer should not have different colors that don’t match my logo
• It shouldn’t be made without having my Instagram or website on the flyer

```html
<!DOCTYPE html>
<html lang="en">
<head>
<meta charset="utf-8">
<title>Luze Kora Wigs – Thank You Postcard</title>
<link rel="stylesheet" href="https://fonts.googleapis.com/css2?family=Mrs+Saint+Delafield&family=Lato:wght@400;600;700&family=Open+Sans:ital,wght@0,300;0,400;1,400&display=swap">
<style>
  :root {
    --pink: #e34398;
    --ink: #4a4a4a;
    --ink-soft: #5a5a5a;
    --paper: #ffffff;
    --backdrop: #ffffd2;
    --silver-light: #cfcfcf;
    --silver-dark: #959595;
  }
  html, body {
    margin: 0;
    width: 1200px;
    height: 1200px;
    overflow: hidden;
    background: var(--backdrop);
  }
  .postcards { display: block; width: 1200px; height: 1200px; }
  .card { fill: var(--paper); }
  .script-title { font-family: "Mrs Saint Delafield", cursive; fill: var(--pink); }
  .headline {
    font-family: "Lato", sans-serif; font-weight: 600; fill: var(--pink);
    stroke: var(--paper); stroke-width: 4px; paint-order: stroke;
  }
  .brand-name { font-family: "Lato", sans-serif; font-weight: 600; fill: var(--pink); }
  .connect-label { font-family: "Lato", sans-serif; font-weight: 400; fill: var(--pink); }
  .rule { stroke: var(--pink); stroke-width: 2.5; }
  .contact { font-family: "Open Sans", sans-serif; font-style: italic; fill: var(--ink); }
  .icon-ring { fill: none; stroke: var(--pink); stroke-width: 1.6; }
  .tip { font-family: "Open Sans", sans-serif; font-weight: 300; font-size: 13.5px; fill: var(--ink-soft); }
  .tip-heading { font-family: "Lato", sans-serif; font-weight: 600; font-size: 13.5px; fill: var(--ink); }
  .tick { fill: none; stroke: var(--pink); stroke-width: 2; stroke-linecap: round; stroke-linejoin: round; }
  .footer-band { fill: var(--pink); }
  .footer-text { font-family: "Open Sans", sans-serif; font-weight: 400; font-size: 22px; fill: var(--paper); }
  .footer-handle { font-family: "Open Sans", sans-serif; font-style: italic; font-size: 29px; fill: var(--paper); }
  .footer-ring { fill: none; stroke: var(--paper); stroke-width: 1.8; }
</style>
</head>
<body>
<svg class="postcards" viewBox="0 0 1200 1200" xmlns="http://www.w3.org/2000/svg">
  <defs>
    <linearGradient id="silver" x1="0" y1="0" x2="1" y2="1">
      <stop offset="0" stop-color="var(--silver-light)"/>
      <stop offset="0.5" stop-color="var(--silver-dark)"/>
      <stop offset="1" stop-color="var(--silver-light)"/>
    </linearGradient>
    <g id="tick"><path class="tick" d="M0 3 L3 6 L8 -2"/></g>
  </defs>

  <!-- Front: thank you side -->
  <g class="front">
    <rect class="card" x="256" y="50" width="696" height="519"/>
    <rect class="glitter-band" x="256" y="231" width="696" height="117" fill="url(#silver)" role="img" aria-label="Silver glitter band"/>
    <text class="script-title" x="604" y="200" font-size="118" text-anchor="middle">Thank You</text>
    <text class="headline" x="593" y="322" font-size="88" text-anchor="middle">For Shopping</text>

    <text class="brand-name" x="415" y="430" font-size="34" text-anchor="middle">Luze Kora</text>
    <text class="brand-name" x="415" y="470" font-size="34" text-anchor="middle">Wigs</text>

    <line class="rule" x1="579" y1="424" x2="624" y2="424"/>
    <line class="rule" x1="866" y1="424" x2="911" y2="424"/>
    <text class="connect-label" x="745" y="432" font-size="25" text-anchor="middle">STAY CONNECTED</text>

    <circle class="icon-ring" cx="671" cy="461" r="9"/>
    <text class="contact" x="686" y="469" font-size="22">@luze.kora.wigs__</text>
    <circle class="icon-ring" cx="645" cy="495" r="9"/>
    <text class="contact" x="660" y="503" font-size="22">www.luzekorawigs.example</text>
  </g>

  <!-- Back: hair care tips side -->
  <g class="back">
    <rect class="card" x="256" y="604" width="696" height="519"/>
    <text class="script-title" x="592" y="708" font-size="92" text-anchor="middle">Hair Care Tips</text>

    <g class="tips">
      <use href="#tick" x="289" y="750"/><text class="tip" x="307" y="759">Apply a moisture rich Conditioner and comb hair, starting with the ends working your way up to your scalp.</text>
      <use href="#tick" x="289" y="766"/><text class="tip" x="307" y="775">Leave Conditioner in for at least 15 minutres or more</text>
      <use href="#tick" x="289" y="782"/><text class="tip" x="307" y="791">Do not massage the hair</text>
      <use href="#tick" x="289" y="798"/><text class="tip" x="307" y="807">Rinse thoroughly</text>
      <use href="#tick" x="289" y="814"/><text class="tip" x="307" y="823">Scrunch hair gently to ehnance the curs. (For wavy/curly patterns)</text>
      <use href="#tick" x="289" y="830"/><text class="tip" x="307" y="839">When damp, apply a dime size of an anti-frizz alcohol free hair serum.</text>
      <use href="#tick" x="289" y="846"/><text class="tip" x="307" y="855">Let air-dry</text>
      <use href="#tick" x="289" y="862"/><text class="tip" x="307" y="871">Do not use oil products or excessive products on curly hair, it will cause matting.</text>
      <use href="#tick" x="289" y="878"/><text class="tip" x="307" y="887">Do not brush or comb hair when dry, it will cause hair to frizz and may cause hair to tangle.</text>

      <text class="tip-heading" x="307" y="920">BED TIME CARE</text>
      <use href="#tick" x="289" y="927"/><text class="tip" x="307" y="936">Before going to bed, braid your hair into one loose large braid and wear a sating scarf or bonnet.</text>
      <use href="#tick" x="289" y="943"/><text class="tip" x="307" y="952">After waking up, undo braid and comb using a wide tooth comb (or paddle brush) through begining at the</text>
      <text class="tip" x="307" y="968">ends and working your way up to roots.</text>
      <use href="#tick" x="289" y="975"/><text class="tip" x="307" y="984">Style as needed.</text>
    </g>

    <rect class="glitter-band" x="256" y="1011" width="696" height="112" fill="url(#silver)" role="img" aria-label="Silver glitter border"/>
    <rect class="footer-band" x="256" y="1038" width="696" height="59"/>
    <text class="footer-text" x="357" y="1072">Tags us on instagram</text>
    <circle class="footer-ring" cx="596" cy="1065" r="10"/>
    <text class="footer-handle" x="617" y="1076">@luze.kora.wigs__</text>
  </g>
</svg>
</body>
</html>
```